Poster Design for kebab shop products

need a new poster for our new velmo pack special, sign will be inside of shopping centre at different location to shop will need to stand out and draw customers to the store, MUST contain shops logo & picture added, poster size will be 76cm x 101cm so will need to suit that size

MUST ALSO CONTAIN THE FOLLOWING
Velmo Pack / HSP
Lamb & Chips
Chicken & Chips
Beef & Chips
+ Can $15

Target Market(s)

new customers

Industry/Entity Type

Retail

Font styles to use
Sans Serif

Colors

Designer to choose colors to be used in the design.

Requirements
Must have
• company logo
• picture of vemo pack provided
• Velmo Pack / HSP
• Lamb & Chips
• Chicken & Chips
• Beef & Chips
• + Can $15

```html
<!DOCTYPE html>
<html lang="en">
<head>
<meta charset="utf-8">
<title>Velmo Pack / HSP Poster</title>
<link href="https://fonts.googleapis.com/css2?family=Nunito+Sans:wght@700;800;900&display=swap" rel="stylesheet">
<style>
  :root {
    --orange-deep: #b9420f;
    --orange-mid: #e0781c;
    --orange-glow: #f3b24a;
    --wood-light: #b98f66;
    --wood-dark: #6b4a32;
    --tray-light: #f2f0ec;
    --tray-food: #c9924a;
    --white: #ffffff;
    --band-orange: #f39a1e;
    --brand-ink: #5a3a22;
  }
  * { margin: 0; padding: 0; box-sizing: border-box; }
  html, body { width: 903px; height: 1200px; overflow: hidden; background: var(--white); }
  .poster {
    position: relative;
    width: 903px;
    height: 1200px;
    overflow: hidden;
    font-family: "Nunito Sans", Arial, sans-serif;
    background: radial-gradient(ellipse at 50% 55%, var(--orange-glow) 0%, var(--orange-mid) 45%, var(--orange-deep) 100%);
  }
  .headline {
    position: absolute;
    top: 44px;
    left: 0;
    width: 100%;
    text-align: center;
    color: var(--white);
  }
  .headline__title {
    font-size: 90px;
    font-weight: 800;
    line-height: 1;
    letter-spacing: 0.5px;
  }
  .headline__items {
    margin-top: 26px;
    list-style: none;
    font-size: 55px;
    font-weight: 900;
    line-height: 68px;
  }
  .scene {
    position: absolute;
    inset: 0;
  }
  .brand {
    position: absolute;
    left: 470px;
    top: 1100px;
    width: 380px;
    text-align: center;
    font-size: 46px;
    font-weight: 900;
    line-height: 1;
    color: var(--brand-ink);
  }
</style>
</head>
<body>
<main class="poster">
  <svg class="scene" width="903" height="1200" viewBox="0 0 903 1200">
    <defs>
      <linearGradient id="woodTone" x1="0" y1="0" x2="0" y2="1">
        <stop offset="0" stop-color="var(--wood-light)"/>
        <stop offset="1" stop-color="var(--wood-dark)"/>
      </linearGradient>
      <linearGradient id="foodTone" x1="0" y1="0" x2="0" y2="1">
        <stop offset="0" stop-color="var(--tray-light)"/>
        <stop offset="0.45" stop-color="var(--tray-light)"/>
        <stop offset="0.55" stop-color="var(--tray-food)"/>
        <stop offset="1" stop-color="var(--tray-light)"/>
      </linearGradient>
    </defs>
    <path class="scene__table" role="img" aria-label="Rustic wooden table surface"
          d="M0 640 Q300 500 903 515 L903 1200 L0 1200 Z" fill="url(#woodTone)"/>
    <rect class="scene__meal" role="img" aria-label="Open foam takeaway box with chips topped with kebab meat and garlic and chilli sauces"
          x="268" y="455" width="415" height="440" rx="24" fill="url(#foodTone)"/>
    <path class="scene__band" d="M80 1200 Q300 960 903 940 L903 965 Q330 985 110 1200 Z" fill="var(--band-orange)"/>
    <path class="scene__footer" d="M110 1200 Q330 985 903 965 L903 1200 Z" fill="var(--white)"/>
  </svg>

  <header class="headline">
    <h1 class="headline__title">Velmo Pack / HSP</h1>
    <ul class="headline__items">
      <li>Lamb &amp; Chips</li>
      <li>Chicken &amp; Chips</li>
      <li>Beef &amp; Chips + Can $15</li>
    </ul>
  </header>

  <div class="brand">Grill Haven</div>
</main>
</body>
</html>
```